Family Ranch with a hobby vineyard needs 2 wine labels for our first harvest

Design 2 wine labels (front and back) with the Brindor Ranch logo.
Label 1:
Sauvignon Blanc
Alc. 12.5% by Vol.
Calder Cove Peninsula - add as the region
Year 2022
Label 2:
Cabernet Sauvignon
Alc. 13.5% by Vol.
Year 2022
For the back label design:
GOVERNMENT WARNING: (1) According to the Surgeon General, women
should not drink alcoholic beverages during pregnancy because of the risk of
birth defects. (2) Consumption of alcoholic beverages impairs your ability to
drive a car or operate machinery, and may cause health problems.
Contains Sulfates.
750ML
I just received the bottles and have attached a picture.
Look and feel
Each slider illustrates characteristics of the customer's brand and the style your logo design should communicate.

```html
<!DOCTYPE html>
<html lang="en">
<head>
<meta charset="utf-8">
<title>Brindor Ranch Wine Labels</title>
<link rel="stylesheet" href="https://fonts.googleapis.com/css2?family=Lora:ital,wght@0,400;0,500;1,400&display=swap">
<style>
  :root {
    --backdrop: #d9d6cf;
    --label: #ebe8e1;
    --label-edge: #d3cfc6;
    --ink: #3b3a38;
    --ink-soft: #5a5855;
    --sketch-light: #e2ded6;
    --sketch-dark: #8c8984;
  }
  * { box-sizing: border-box; margin: 0; padding: 0; }
  html, body {
    width: 1200px;
    height: 884px;
    overflow: hidden;
    background: var(--backdrop);
  }
  .label-set {
    width: 1200px;
    height: 884px;
    display: flex;
    align-items: center;
    justify-content: center;
    gap: 52px;
  }
  .label {
    background: var(--label);
    border: 1px solid var(--label-edge);
    color: var(--ink);
    font-family: "Lora", serif;
    display: flex;
    flex-direction: column;
    align-items: center;
    text-align: center;
  }
  .label--front { width: 252px; height: 404px; padding: 30px 22px 26px; }
  .label--back  { width: 222px; height: 318px; padding: 32px 20px 22px; margin-top: 60px; }

  .brand {
    display: flex;
    flex-direction: column;
    align-items: center;
    gap: 8px;
  }
  .brand__dot {
    width: 26px;
    height: 26px;
    border-radius: 50%;
    background: var(--ink);
  }
  .brand__name {
    font-family: "Lora", serif;
    font-weight: 500;
    font-size: 17px;
    letter-spacing: 1.5px;
    text-transform: uppercase;
    color: var(--ink);
  }
  .label--back .brand__dot { width: 22px; height: 22px; }
  .label--back .brand__name { font-size: 15px; }

  .varietal {
    margin-top: 22px;
    font-size: 14px;
    font-weight: 400;
    letter-spacing: 0.5px;
    text-transform: uppercase;
  }
  .vintage {
    margin-top: 12px;
    padding: 2px 12px;
    border: 1px solid var(--ink-soft);
    font-size: 9px;
    letter-spacing: 0.6px;
    text-transform: uppercase;
  }
  .sketch {
    margin-top: 18px;
    width: 190px;
    height: 150px;
    border-radius: 46% 46% 40% 40%;
    background: radial-gradient(ellipse at 50% 65%, var(--sketch-dark) 0%, #b3afa9 38%, var(--sketch-light) 72%, var(--label) 100%);
  }
  .abv {
    margin-top: auto;
    font-size: 9px;
    letter-spacing: 0.4px;
    text-transform: uppercase;
  }

  .warning-title {
    margin-top: 24px;
    font-size: 7.5px;
    letter-spacing: 0.4px;
    text-transform: uppercase;
  }
  .warning-text {
    margin-top: 12px;
    font-style: italic;
    font-size: 7.5px;
    line-height: 1.4;
    color: var(--ink-soft);
  }
  .warning-text + .warning-text { margin-top: 9px; }
  .producer {
    margin-top: auto;
    font-size: 6.5px;
    line-height: 1.45;
    color: var(--ink-soft);
  }
</style>
</head>
<body>
<main class="label-set">

  <section class="label label--back" aria-label="Sauvignon Blanc back label">
    <div class="brand"><span class="brand__dot"></span><span class="brand__name">Brindor Ranch</span></div>
    <p class="warning-title">Government Warning:</p>
    <p class="warning-text">(1) According to the Surgeon General, women should not drink alcoholic beverages during pregnancy because of the risk of birth defects.</p>
    <p class="warning-text">(2) Consumption of alcoholic beverages impairs your ability to drive a car or operate machinery, and may cause health problems.</p>
    <p class="producer">Produced and bottled by :<br>Family Ranch with a hobby vineyard<br>Calder Cove Peninsula</p>
  </section>

  <section class="label label--front" aria-label="Sauvignon Blanc front label">
    <div class="brand"><span class="brand__dot"></span><span class="brand__name">Brindor Ranch</span></div>
    <h2 class="varietal">Sauvignon Blanc</h2>
    <p class="vintage">Year 2022</p>
    <div class="sketch" role="img" aria-label="Ink sketch of a lighthouse on rocks with waves and birds"></div>
    <p class="abv">Alc. 12.5% by Vol.</p>
  </section>

  <section class="label label--front" aria-label="Cabernet Sauvignon front label">
    <div class="brand"><span class="brand__dot"></span><span class="brand__name">Brindor Ranch</span></div>
    <h2 class="varietal">Cabernet Sauvignon</h2>
    <p class="vintage">Year 2022</p>
    <div class="sketch" role="img" aria-label="Ink sketch of a lighthouse on rocks with waves and birds"></div>
    <p class="abv">Alc. 13.5% by Vol.</p>
  </section>

  <section class="label label--back" aria-label="Cabernet Sauvignon back label">
    <div class="brand"><span class="brand__dot"></span><span class="brand__name">Brindor Ranch</span></div>
    <p class="warning-title">Government Warning:</p>
    <p class="warning-text">(1) According to the Surgeon General, women should not drink alcoholic beverages during pregnancy because of the risk of birth defects.</p>
    <p class="warning-text">(2) Consumption of alcoholic beverages impairs your ability to drive a car or operate machinery, and may cause health problems.</p>
    <p class="producer">Produced and bottled by :<br>Family Ranch with a hobby vineyard<br>Calder Cove Peninsula</p>
  </section>

</main>
</body>
</html>
```